Product and Services Brochure for an Oil and Gas Business

Need a brochure design for our Products and Services. I've attached expectations, Product Names, Picture link, Logo. Please ask if you have any questions.

Use Black and/or White background and related bright colors per our logo colors. Design will have black silk laminate and SPOT UV. Hence please define the respective layers and incorporate those feature in the design. Be bold, modern and unique. No cluttered designs.

Pictures link https://files.brindlevault.net/share/7QkT2mWz9pLx4RcVn8JdYe3HsGa6bUo?view=open

Logos - There are two logos that we use. One for square spaces and one for horizontal spaces

Target Market(s)

Industrial

Colors

Designer to choose colors to be used in the design.

Requirements
Must have
• Clean, uncluttered and bold design with good color pairing
Nice to have
• Pictures provided have both black and transparent backgrounds. It will be great (not sure how) but keep the background dynamic so no product pic gets lost or have weird lines
Should not have
• Too much color

```html
<!DOCTYPE html>
<html lang="en">
<head>
<meta charset="utf-8">
<title>Products Brochure – Inside Spread</title>
<link rel="stylesheet" href="https://fonts.googleapis.com/css2?family=Montserrat:wght@400;500;700&display=swap">
<style>
  :root{
    --blue:#2b68a6;
    --blue-dark:#1f5690;
    --blue-light:#3d7fbf;
    --green:#80bd41;
    --green-light:#9acb55;
    --black:#000;
    --white:#fff;
    --paper:#f4f4f4;
    --ink:#1c1c1c;
    --stage:#e6e6e6;
  }
  *{box-sizing:border-box;margin:0;padding:0}
  html,body{width:1200px;height:800px;overflow:hidden;background:var(--stage)}
  .spread{position:relative;width:1200px;height:800px;background:var(--white);font-family:"Montserrat",sans-serif;overflow:hidden}
  .waves{position:absolute;inset:0}
  .fold{position:absolute;top:0;bottom:0;width:1px;background:rgba(0,0,0,.08)}
  .fold--one{left:400px}.fold--two{left:800px}

  .info{position:absolute}
  .info__title{color:var(--blue);font-weight:700;font-size:26px;letter-spacing:.3px}
  .info__mark{display:block;width:18px;height:6px;margin:6px 0 10px 4px}
  .info__text{color:var(--ink);font-size:13px;line-height:1.45;font-weight:500}
  .checklist{list-style:none;margin-top:14px}
  .checklist li{position:relative;padding-left:22px;font-size:13.5px;font-weight:500;line-height:1.55;color:var(--blue)}
  .checklist li::before{content:"";position:absolute;left:2px;top:5px;width:6px;height:10px;border:solid var(--green);border-width:0 2px 2px 0;transform:rotate(40deg)}
  .checklist--light li{color:var(--white)}
  .checklist--light li::before{border-color:var(--white)}

  .info--left{left:42px;top:60px;width:340px}
  .info--middle{left:440px;top:44px;width:340px}
  .info--right{left:840px;top:36px;width:320px}

  .product-tag{position:absolute;background:var(--green);color:var(--white);font-weight:700;font-size:20px;letter-spacing:.6px;padding:6px 18px}
  .product-tag--geo{left:190px;top:590px}
  .product-tag--transmitter{left:450px;top:432px}
  .product-tag--caliper{left:880px;top:300px}

  .product-photo{position:absolute;border-radius:8px;background:radial-gradient(ellipse at 40% 40%,#4a4a4a 0%,#222 55%,#0b0b0b 100%)}
  .product-photo--geo{left:70px;top:560px;width:200px;height:150px}
  .product-photo--transmitter{left:470px;top:488px;width:270px;height:110px;background:linear-gradient(90deg,#2a2a2a,#e9e9e9 20%,#2a2a2a 35%,#e9e9e9 55%,#2a2a2a 70%,#e9e9e9 85%,#1a1a1a)}
  .product-photo--caliper{left:880px;top:355px;width:240px;height:100px}

  .contact{position:absolute;left:545px;top:700px;color:var(--white);font-size:16px;font-weight:500;line-height:1.7}
  .contact__row{display:flex;align-items:center;gap:8px}
  .contact__icon{width:15px;height:15px}

  .info--benefits{left:850px;top:560px;width:320px}
</style>
</head>
<body>
<main class="spread">
  <svg class="waves" viewBox="0 0 1200 800" width="1200" height="800" aria-hidden="true">
    <defs>
      <linearGradient id="blueBand" x1="0" y1="0" x2="1" y2="1">
        <stop offset="0" stop-color="#3d7fbf"/>
        <stop offset="1" stop-color="#1f5690"/>
      </linearGradient>
      <linearGradient id="greenBand" x1="0" y1="0" x2="1" y2="0">
        <stop offset="0" stop-color="#7cba3d"/>
        <stop offset="1" stop-color="#9acb55"/>
      </linearGradient>
    </defs>
    <!-- green ribbon -->
    <path d="M0,530 C150,455 300,415 400,395 C550,370 700,305 800,275 C950,225 1080,175 1200,145 L1200,800 L0,800 Z" fill="url(#greenBand)"/>
    <!-- black field -->
    <path d="M0,555 C150,480 300,440 400,420 C550,395 700,330 800,300 C950,250 1080,200 1200,170 L1200,800 L0,800 Z" fill="#000"/>
    <!-- white rim -->
    <path d="M0,736 C150,706 300,691 400,686 C550,676 700,606 800,566 C950,506 1080,436 1200,386 L1200,800 L0,800 Z" fill="#f4f4f4"/>
    <!-- blue base -->
    <path d="M0,750 C150,720 300,705 400,700 C550,690 700,620 800,580 C950,520 1080,450 1200,400 L1200,800 L0,800 Z" fill="url(#blueBand)"/>
  </svg>

  <span class="fold fold--one"></span>
  <span class="fold fold--two"></span>

  <section class="info info--left">
    <h2 class="info__title">Product Info</h2>
    <svg class="info__mark" viewBox="0 0 18 6"><path d="M0,6 L9,0 L18,6 L9,3 Z" fill="#80bd41"/></svg>
    <p class="info__text">Lorem ipsum dolor sit amet, consectetur adipiscing elit, sed do eiusmod tempor incididunt ut labore et dolore magna aliqua.</p>
    <ul class="checklist">
      <li>Lorem ipsum dolor sit amet</li>
      <li>Consectetur adipiscing elit</li>
      <li>Sed do eiusmod tempor incididunt</li>
      <li>Ut labore et dolore</li>
      <li>Sed do eiusmod tempor</li>
      <li>Lorem ipsum dolor sit amet</li>
    </ul>
  </section>

  <section class="info info--middle">
    <h2 class="info__title">Product Info</h2>
    <svg class="info__mark" viewBox="0 0 18 6"><path d="M0,6 L9,0 L18,6 L9,3 Z" fill="#80bd41"/></svg>
    <p class="info__text">Lorem ipsum dolor sit amet, consectetur adipiscing elit, sed do eiusmod tempor incididunt ut labore et dolore magna aliqua.</p>
    <ul class="checklist">
      <li>Lorem ipsum dolor sit amet</li>
      <li>Consectetur adipiscing elit</li>
      <li>Sed do eiusmod tempor incididunt</li>
      <li>Ut labore et dolore</li>
    </ul>
  </section>

  <section class="info info--right">
    <h2 class="info__title">Product Info</h2>
    <svg class="info__mark" viewBox="0 0 18 6"><path d="M0,6 L9,0 L18,6 L9,3 Z" fill="#80bd41"/></svg>
    <p class="info__text">Lorem ipsum dolor sit amet, consectetur adipiscing elit, sed do eiusmod tempor incididunt ut labore et dolore magna aliqua.</p>
  </section>

  <div class="product-photo product-photo--geo" role="img" aria-label="Product photo: black pipeline geo-locating tool with red remove-before-flight tag"></div>
  <span class="product-tag product-tag--geo">VT-GEO</span>

  <span class="product-tag product-tag--transmitter">VT-Transmitter</span>
  <div class="product-photo product-photo--transmitter" role="img" aria-label="Product photo: three cylindrical transmitters in decreasing sizes"></div>

  <span class="product-tag product-tag--caliper">VT-CALIPER</span>
  <div class="product-photo product-photo--caliper" role="img" aria-label="Product photo: black caliper pipeline tool with two cups"></div>

  <address class="contact" style="font-style:normal">
    <div class="contact__row">
      <svg class="contact__icon" viewBox="0 0 16 16"><circle cx="8" cy="8" r="7" fill="none" stroke="#fff" stroke-width="1.3"/><path d="M5.5,4.5 L7,4.5 L7.6,6.3 L6.8,7 C7.2,8 8,8.8 9,9.2 L9.7,8.4 L11.5,9 L11.5,10.5 C8,10.8 5.2,8 5.5,4.5 Z" fill="#fff"/></svg>
      <span>281-555-0148</span>
    </div>
    <div class="contact__row">
      <svg class="contact__icon" viewBox="0 0 16 16" fill="none" stroke="#fff" stroke-width="1.3"><circle cx="8" cy="8" r="7"/><ellipse cx="8" cy="8" rx="3" ry="7"/><path d="M1,8 H15 M2.5,4.5 H13.5 M2.5,11.5 H13.5"/></svg>
      <span>www.pipelinetrack.example</span>
    </div>
  </address>

  <section class="info info--benefits">
    <ul class="checklist checklist--light">
      <li>Lorem ipsum dolor sit amet</li>
      <li>Consectetur adipiscing elit</li>
      <li>Sed do eiusmod tempor incididunt</li>
      <li>Ut labore et dolore</li>
      <li>Sed do eiusmod tempor</li>
      <li>Lorem ipsum dolor sit amet</li>
    </ul>
  </section>
</main>
</body>
</html>
```